Occupational Therapy promotional poster

We need 2 x A4 posters to be created:
- 1 with a male super hero
- 1 with a female super hero (see suggested design).

These posters will be used for a promotional campaign celebrating occupational therapy. The idea being that occupational therapists are our local superhero. We see them as the ‘unsung heroes’ of our local communities, so this campaign is a play on that idea.

These posters will be displayed on community notice boards and in hospitals. They will also be used on display tables promoting what occupational therapy is. They will also potentially be used as handouts in presentations. We plan to use these posters for the coming 2 years.

As these will be displayed on noticeboards they need to be bright and colourful. The colours suggested in the attachment are the types of colours we would like used (blue, yellow and red).

We envision these posters being displayed side by side.

Although we are open to interpretation of the “super hero” theme – we particularly liked the black super hero images as they look similar to the symbol for wheelchair access (which occupational therapists use).

Alternatively, a comic book inspired design would also be appealing – see inspiration images in attached document.

See the images that we have drawn inspiration from. I've included the black generic super heroes as well as the comic book style.

This design needs to include the KLRV-PTB logo which is included.

The superhero also needs to have a starwarden style logo somewhere visable. This could be on their chest or on their cape – depending on their angle. Instead of the Starwarden ‘S’, please put ‘OT’.

The content for both posters is identical. However, we would like 1 male version of the poster and 1 female version of the poster.

The superhero graphic needs to be G-rated. For the female graphic - it cannot include cleavage or clothing that is too tight/revealing.

Based on the locations where the poster will be displayed, it does need to have a professional feel.

ATTACHED:
- the KLRV-PTB Logo (to be included)
- a design brief + all text that needs to be included
- an example of the type of posters that we are envisioning

Target Market(s)

General public in New Zealand: Patients in hospital waiting rooms, mothers of children in childcare, elderly people who look at notice boards

Industry/Entity Type

Health Care

Font styles to use
Sans Serif

Requirements
Must have
• 2 A4 twin posters. Identical content but 1 female version and 1 male version
• The KLRV-PTB logo (attached)
• A "superhero" symbol on the chest or cape of the superhero. It should look like the starwarden symbol but instead say "OT" rather than S.
• Must be bright and colourful
• Must include all text included
Should not have
• Any nudity, revealing poses or tight clothing. G-rated.

```html
<!DOCTYPE html>
<html lang="en">
<head>
<meta charset="utf-8">
<title>Meet Your Local Superhero – The Occupational Therapist</title>
<link href="https://fonts.googleapis.com/css2?family=Oswald:wght@500;700&family=Open+Sans:ital,wght@0,400;0,700;1,400;1,700&display=swap" rel="stylesheet">
<style>
:root{
  --blue:#1b6db5;
  --blue-dark:#124f8a;
  --green:#56a52f;
  --lime:#b7d433;
  --yellow:#f3e45a;
  --ink:#2c3440;
  --paper:#ffffff;
}
*{box-sizing:border-box;margin:0;padding:0}
html,body{width:870px;height:1200px;overflow:hidden;background:var(--paper)}
body{font-family:"Open Sans",Arial,sans-serif;color:var(--ink)}
.poster{position:relative;width:870px;height:1200px;background:var(--paper);overflow:hidden}
.top-stripe{height:16px;background:linear-gradient(90deg,var(--blue),var(--green))}
.headline{
  font-family:"Oswald",Impact,sans-serif;font-weight:700;text-transform:uppercase;
  font-style:italic;transform:skewX(-6deg);
}
.title{
  margin:26px 0 0;text-align:center;font-size:64px;line-height:1;letter-spacing:1px;
  background:linear-gradient(90deg,var(--green),var(--blue));
  -webkit-background-clip:text;background-clip:text;color:transparent;
}
.band{
  margin-top:18px;background:var(--blue);color:#fff;text-align:center;
  padding:14px 0 16px;
}
.band .headline{font-size:50px;line-height:1;display:block}
.intro{padding:26px 70px 0}
.lead{font-style:italic;font-weight:700;font-size:15.5px;line-height:1.45;color:var(--ink);margin-bottom:16px}
.section-heading{font-family:"Oswald",Impact,sans-serif;font-weight:700;color:var(--green);
  text-transform:uppercase;font-size:21px;line-height:1.2;margin-bottom:6px}
.body-copy{font-size:13.5px;line-height:1.5;margin-bottom:16px}
.profile{display:flex;padding:8px 50px 0 50px;gap:24px;height:500px}
.hero-art{
  width:300px;height:470px;border-radius:140px 140px 20px 20px;
  background:radial-gradient(circle at 50% 40%,#3a3f46 0%,#1c1f24 70%);
}
.profile-copy{flex:1;text-align:center}
.profile-title{font-size:48px;color:var(--blue);line-height:1;margin-top:6px}
.profile-intro{font-weight:700;font-size:17px;margin:12px 0 10px}
.powers{list-style:none}
.powers li{font-size:14px;line-height:1.35;padding:4px 0}
.footer{
  position:absolute;left:0;bottom:0;width:870px;height:150px;
  background:linear-gradient(180deg,var(--yellow),var(--lime));
  display:flex;align-items:center;justify-content:space-between;padding:0 50px;
}
.footer-copy{font-size:16px;line-height:1.5}
.footer-copy strong{color:var(--blue-dark)}
.hashtag{color:var(--blue-dark);font-weight:700}
.site{font-weight:700;color:var(--blue-dark)}
.brand{display:flex;align-items:center;gap:10px}
.brand-dot{width:34px;height:34px;border-radius:50%;background:var(--blue)}
.brand-name{font-family:"Open Sans",Arial,sans-serif;font-weight:700;font-size:26px;color:var(--blue-dark)}
</style>
</head>
<body>
<main class="poster">
  <div class="top-stripe"></div>
  <h1 class="title headline">Meet your local superhero</h1>
  <div class="band"><span class="headline">The occupational therapist</span></div>

  <section class="intro">
    <p class="lead">Imagine being defeated by an everyday task like putting your clothes on, catching a bus, spending time with your friends or taking care of yourself.</p>
    <h2 class="section-heading">Occupational therapy is here to help</h2>
    <p class="body-copy">The things that you do – your occupations – help express who you are, how you feel about yourself, and how you connect with others. Your health and wellbeing will be affected if you are unable to do the things you want and need to do, to live and enjoy your life.</p>
    <h2 class="section-heading">Occupational therapists help people of all ages and work in a variety of settings</h2>
    <p class="body-copy">The things that you do – your occupations – help express who you are, how you feel about yourself, and how you connect with others. Your health and wellbeing will be affected if you are unable to do the things you want and need to do, to live and enjoy your life.</p>
  </section>

  <section class="profile">
    <div class="hero-art" role="img" aria-label="Silhouette of a caped superhero with a red and green OT shield emblem on the chest"></div>
    <div class="profile-copy">
      <h2 class="profile-title headline">Superhero profile</h2>
      <p class="profile-intro">My super powers help people to:</p>
      <ul class="powers">
        <li>Learn new ways of doing things following an illness or injury (e.g. dressing or cooking)</li>
        <li>Thrive in their senior years</li>
        <li>Regulate their strong emotions</li>
        <li>Achieve their goals at school</li>
        <li>Develop ways to manage pain</li>
        <li>Develop their confidence in social situations</li>
        <li>Access support available in the community</li>
        <li>Adapt material or equipment (e.g. wheelchairs or provide a special bath or toilet seat)</li>
        <li>Make changes to their living or working environment</li>
        <li>Develop new skills, abilities or interests (e.g. job readiness programmes)</li>
      </ul>
    </div>
  </section>

  <footer class="footer">
    <div class="footer-copy">
      <p><strong>JOIN US</strong> in celebrating occupational therapy by using the hashtag<br><span class="hashtag">#YourLocalSuperHero</span></p>
      <p>Visit <span class="site">klrvptb.co.nz</span> for more information</p>
    </div>
    <div class="brand">
      <span class="brand-dot"></span>
      <span class="brand-name">KLRV-PTB</span>
    </div>
  </footer>
</main>
</body>
</html>
```